Optometry office needs a postcard to get name out to local schools

I need a postcard design for an optometry office called "Hosaru Optometry".
I want to get our name out to local schools and with this short letter and advertisement.
I want to keep the baby blue /navy blue colors theme.
One the front i want the following
Front:
1) three lines for the address of the recipient as in the example, and square for the postage in the upper right hand corner.
2) our logo with "Hosaru Optometry" and a horizontal line with our website address just below the line as in the example.
put the words "Our practice is committed to supporting our community and local schools." and our phone number "714-390-5264"
3) perhaps more contact info is looks neat and not too cluttered
Back:
1) letter which is attached
2) maybe a small clip art like a phoropter or glasses or something eye related

```html
<!DOCTYPE html>
<html lang="en">
<head>
<meta charset="utf-8">
<title>Hosaru Optometry – School Postcard</title>
<link rel="stylesheet" href="https://fonts.googleapis.com/css2?family=EB+Garamond:wght@400&family=Questrial&family=Roboto+Condensed:wght@700&family=Tinos&family=Roboto:wght@400;500&display=swap">
<style>
  :root {
    --baby-blue: #5cc0e3;
    --baby-blue-soft: #a9dcef;
    --sky-text: #7dcbe8;
    --navy: #27318a;
    --ink: #3d3d3d;
    --grey-text: #c6c6c6;
    --backdrop: #e9ecef;
    --white: #ffffff;
  }
  * { box-sizing: border-box; margin: 0; padding: 0; }
  html, body { width: 1200px; height: 1000px; overflow: hidden; }
  body { background: var(--backdrop); position: relative; font-family: "Questrial", sans-serif; }

  .postcard { position: absolute; background: var(--white); box-shadow: 0 6px 18px rgba(0,0,0,.18); overflow: hidden; }

  /* Brand lockup */
  .brand { position: absolute; display: flex; align-items: center; gap: 10px; }
  .brand__mark { flex: none; width: 20px; height: 20px; background: var(--baby-blue); }
  .brand__name { font-family: "Questrial", sans-serif; color: var(--navy); font-size: 27px; line-height: 27px; white-space: nowrap; }

  /* Address side */
  .postcard--front { left: 90px; top: 40px; width: 700px; height: 540px; }
  .postcard--front .brand { left: 22px; top: 68px; }
  .front__address { position: absolute; left: 192px; top: 114px; font-family: "Roboto", sans-serif; font-size: 15px; color: var(--grey-text); white-space: nowrap; }
  .postage-box { position: absolute; left: 508px; top: 22px; width: 158px; height: 104px; border: 3px solid #d4d4d4; display: flex; align-items: center; justify-content: center; text-align: center; color: #d0d0d0; font-family: "Roboto", sans-serif; font-size: 18px; line-height: 20px; }
  .front__rule { position: absolute; left: 0; top: 142px; width: 545px; height: 8px; background: linear-gradient(90deg, var(--baby-blue-soft), var(--baby-blue) 55%, rgba(92,192,227,.15)); clip-path: polygon(0 35%, 100% 0, 100% 55%, 0 100%); }
  .front__links { position: absolute; left: 30px; top: 168px; font-family: "Roboto", sans-serif; font-weight: 500; font-size: 16.5px; letter-spacing: .6px; color: var(--sky-text); word-spacing: 8px; white-space: nowrap; }
  .front__panel { position: absolute; left: 0; top: 225px; width: 100%; bottom: 0; background: linear-gradient(90deg, var(--baby-blue) 0%, #7acde9 35%, #def2fa 60%, var(--white) 78%); }
  .front__pledge { position: absolute; left: 30px; top: 250px; font-family: "EB Garamond", serif; font-size: 30px; line-height: 30px; color: var(--white); }
  .front__cta { position: absolute; left: 38px; top: 428px; color: var(--white); }
  .front__cta-label { font-family: "Roboto Condensed", sans-serif; font-weight: 700; font-size: 27px; letter-spacing: .3px; }
  .front__cta-phone { font-family: "Roboto", sans-serif; font-size: 27px; letter-spacing: .8px; }

  /* Letter side */
  .postcard--back { left: 420px; top: 398px; width: 713px; height: 509px; background: linear-gradient(180deg, #b8e2f2 0%, #e4f4fb 28%, var(--white) 60%); }
  .back__address { position: absolute; left: 48px; top: 26px; font-family: "Roboto", sans-serif; font-size: 14.5px; line-height: 16px; color: #52b3dc; }
  .back__links { position: absolute; right: 315px; top: 42px; text-align: right; font-family: "Roboto", sans-serif; font-weight: 500; font-size: 14px; line-height: 17px; color: var(--navy); white-space: nowrap; }
  .back__rule { position: absolute; left: 48px; top: 86px; width: 362px; height: 6px; background: linear-gradient(90deg, var(--baby-blue), #8fd3ec); }
  .letter { position: absolute; left: 48px; top: 108px; width: 322px; font-family: "Tinos", serif; font-size: 10.6px; line-height: 13.2px; color: var(--ink); }
  .letter p { margin-bottom: 13px; }
  .letter__signature { position: absolute; left: 48px; top: 458px; font-family: "Tinos", serif; font-size: 13px; color: #222; }
  .back__photo { position: absolute; left: 385px; top: 0; width: 360px; height: 330px; border-radius: 50% 0 0 50% / 55% 0 0 55%; background: radial-gradient(ellipse at 55% 50%, #c9cccf 0%, #a9adb2 45%, #dde0e3 80%, rgba(255,255,255,0) 100%); }
  .postcard--back .brand { left: 535px; top: 418px; }
</style>
</head>
<body>

<section class="postcard postcard--front" aria-label="Postcard address side">
  <div class="brand"><span class="brand__mark"></span><span class="brand__name">Hosaru<br>Optometry</span></div>
  <div class="front__address">2270 Maple Grove Rd, #A Cypress, CA 90630</div>
  <div class="postage-box">Affix<br>Postage<br>Here</div>
  <div class="front__rule"></div>
  <div class="front__links">www.hosaruoptometry.com hosaruoptometry@gmail.com</div>
  <div class="front__panel"></div>
  <p class="front__pledge">Our practice<br>is committed<br>to supporting<br>our community<br>and local schools</p>
  <div class="front__cta">
    <div class="front__cta-label">CALL US TODAY</div>
    <div class="front__cta-phone">714-390-5264</div>
  </div>
</section>

<section class="postcard postcard--back" aria-label="Postcard letter side">
  <div class="back__photo" role="img" aria-label="Photo of a smiling child looking through a phoropter trial frame"></div>
  <div class="back__address">2270 Maple Grove Rd,<br>#A Cypress,<br>CA 90630</div>
  <div class="back__links">www.hosaruoptometry.com<br>hosaruoptometry@gmail.com</div>
  <div class="back__rule"></div>
  <div class="letter">
    <p>Dear</p>
    <p>I would like to introduce our family optometry office that has been in business for the past 35 years! We are located at 2270 Maple Grove Rd, Ste A in Cypress (near Maple Grove Rd and Orange Ave).</p>
    <p>Our practice is committed to supporting our community and local schools by taking care of adults and children of all ages. As 80% of learning is done visually, it is especially important for young children to have access to routine comprehensive eye care. Our goal is to provide excellent eye care for families as well as quality ophthalmic frames and lenses at reasonable prices.</p>
    <p>We are happy to see any referrals from you, including students who have not passed vision screenings or have other ocular health concerns. Please feel free to reach out to us if you have any questions. You can contact us by phone or email, and are also welcome to visit our office anytime.</p>
    <p>We look forward to a strong relationship together and success for all your students.</p>
    <p>Sincerely</p>
  </div>
  <div class="letter__signature">Ken Hosaru, OD</div>
  <div class="brand"><span class="brand__mark"></span><span class="brand__name">Hosaru<br>Optometry</span></div>
</section>

</body>
</html>
```